Communication and Marketing agency needs a new presentation card

We are a group of communication and marketing agencies specialized in companies that are in the logistics and industrial sector. The head agency is TELVANO Grupo and the group consists of 4 agencies: TELVANO Media, TELVANO Digital, TELVANO Research and EnlazaPorImagen. We hace 4 offices in Spain (Madrid, Barcelona, Valencia and Murcia). We are looking for a clean and attractive design that transmits our experience, brand presence in the market and knowledge to those who receive the card.It has to maintain the colors of the logo that is attached.
Target Market(s)
logistics and industrial sector
Marketing department
Clean and attractive design

```html
<!DOCTYPE html>
<html lang="en">
<head>
<meta charset="UTF-8">
<title>TELVANO Grupo – Business Card</title>
<link rel="stylesheet" href="https://fonts.googleapis.com/css2?family=Oswald:wght@600&family=PT+Sans:wght@400;700&display=swap">
<style>
  :root {
    --bg: #3a3a3a;
    --card: #1c1c1d;
    --red: #c4242f;
    --grey: #5c5c5e;
    --silver: #8a8a8c;
    --white: #f2f2f2;
  }
  * { margin: 0; padding: 0; box-sizing: border-box; }
  html, body { width: 1200px; height: 900px; overflow: hidden; }
  body {
    background: var(--bg);
    font-family: "PT Sans", sans-serif;
    color: var(--white);
    position: relative;
  }
  .card {
    position: absolute;
    left: 250px;
    width: 700px;
    height: 400px;
    background: var(--card);
    box-shadow: 0 8px 24px rgba(0,0,0,0.45);
  }
  .card--front { top: 25px; }
  .card--back { top: 465px; }

  .brand {
    position: absolute;
    font-family: "PT Sans", sans-serif;
    font-weight: 700;
    font-size: 54px;
    letter-spacing: 1px;
    line-height: 1;
    white-space: nowrap;
  }
  .card--front .brand { color: var(--silver); left: 200px; top: 170px; }
  .card--back .brand { color: var(--red); right: 40px; top: 90px; }

  .person { position: absolute; left: 48px; top: 205px; }
  .person__name {
    font-family: "Oswald", sans-serif;
    font-weight: 600;
    font-size: 34px;
    color: var(--red);
    line-height: 1.05;
    letter-spacing: 0.5px;
  }
  .person__role { font-size: 15px; letter-spacing: 1px; margin-top: 4px; }

  .divider { display: block; margin: 12px 0 14px; }

  .contact { font-size: 17px; line-height: 1.35; }
  .contact__label { font-weight: 700; margin-right: 6px; }

  .office { position: absolute; right: 60px; bottom: 42px; font-size: 17px; line-height: 1.35; }
  .office .divider { margin: 0 0 10px; }
  .accent { color: var(--red); }
</style>
</head>
<body>
  <section class="card card--front">
    <div class="brand">TELVANO Digital</div>
  </section>

  <section class="card card--back">
    <div class="brand">TELVANO Grupo</div>

    <div class="person">
      <div class="person__name">MARCO LEDESMA</div>
      <div class="person__role">MANAGER</div>
      <svg class="divider" width="40" height="8" viewBox="0 0 40 8" aria-hidden="true">
        <circle cx="4" cy="4" r="3.5" fill="var(--red)"/>
        <line x1="4" y1="4" x2="40" y2="4" stroke="var(--red)" stroke-width="1.5"/>
      </svg>
      <div class="contact">
        <div><span class="contact__label">P.</span>+(402) -555- 0148</div>
        <div><span class="contact__label">F.</span>+(402) -555- 0148</div>
        <div>contacto@telvanogrupo.com</div>
      </div>
    </div>

    <div class="office">
      <svg class="divider" width="40" height="8" viewBox="0 0 40 8" aria-hidden="true">
        <circle cx="4" cy="4" r="3.5" fill="var(--red)"/>
        <line x1="4" y1="4" x2="40" y2="4" stroke="var(--red)" stroke-width="1.5"/>
      </svg>
      <div>1840 Calle Alcalá 27th Street,</div>
      <div>Madrid, MD 28014</div>
      <div>www.<span class="accent">telvanogrupo</span>.com</div>
    </div>
  </section>
</body>
</html>
```